Zorpax.com (Dedicated servers Provider)

We provide dedicated servers for clients around the world. We have created a layout for you. You need to create exactly the design based on these sketches. All text, you can take from our sketches (later we will replace them).

Target Market(s)

Web site owners and web developers

Requirements
Should not have
• The design should not use old-style fonts.

```html
<!DOCTYPE html>
<html lang="en">
<head>
<meta charset="utf-8">
<title>Zorpax.com — Dedicated Servers</title>
<link href="https://fonts.googleapis.com/css2?family=Open+Sans:wght@400;600;700;800&display=swap" rel="stylesheet">
<style>
:root{
  --green:#7cbd1e;
  --green-dark:#3f6a0c;
  --green-deep:#2c4a08;
  --orange:#f07c12;
  --orange-dark:#d35f00;
  --ink:#2b2b2b;
  --dark:#1e1e1e;
  --darker:#141414;
  --muted:#9a9a9a;
  --light:#f2f2f2;
  --line:#d9d9d9;
  --red:#d01818;
  --white:#fff;
}
*{box-sizing:border-box;margin:0;padding:0}
html,body{width:691px;height:1200px;overflow:hidden}
body{font-family:"Open Sans",Arial,sans-serif;color:var(--ink);background:var(--white);font-size:8px;line-height:1.35}
a{color:inherit;text-decoration:none}

/* header */
.site-header{height:58px;background:linear-gradient(#2e2e2e,#161616);position:relative;padding:0 18px}
.brand{position:absolute;left:18px;top:12px;display:flex;align-items:center;gap:7px}
.brand-mark{width:22px;height:22px;background:var(--green)}
.brand-name{font-size:24px;font-weight:800;color:var(--white);letter-spacing:.5px}
.call-now{position:absolute;right:18px;top:6px;font-size:12px;font-weight:700;color:var(--white)}
.call-now b{color:var(--green);font-size:14px}
.utility-links{position:absolute;right:18px;top:30px;display:flex;gap:4px}
.utility-links a{background:#3a3a3a;color:#ddd;font-size:7px;padding:2px 8px;border-radius:2px}

/* nav */
.main-nav{height:20px;background:linear-gradient(#3a3a3a,#242424);display:flex;padding-left:72px;gap:2px}
.main-nav a{color:#ddd;font-size:7.5px;font-weight:700;padding:0 11px;line-height:20px;text-transform:uppercase;background:#333;border-left:1px solid #444}
.main-nav a.active{background:var(--green);color:var(--white)}
.main-nav a.order{background:#4a4a4a}

.announcement{margin-top:2px;height:18px;background:var(--green-deep);color:#d8e9bf;font-size:8px;display:flex;align-items:center;padding:0 22px;gap:8px}
.announcement .pin{width:10px;height:10px;border-radius:50%;background:var(--green)}
.announcement a{color:var(--white);font-weight:700;margin-left:6px}

/* hero */
.hero{margin:6px 18px 0;height:222px;background:linear-gradient(#ffffff,#e6e6e6);border:1px solid var(--line);position:relative;overflow:hidden}
.hero-servers{position:absolute;left:20px;top:14px;width:150px;height:180px;background:linear-gradient(#4d5157,#17191c)}
.hero-badge{position:absolute;left:10px;top:120px;width:58px;height:58px;border-radius:50%;background:var(--red);color:var(--white);font-weight:800;font-size:10px;text-align:center;display:flex;align-items:center;justify-content:center;line-height:1.1;transform:rotate(-12deg)}
.hero-copy{position:absolute;left:186px;top:24px;width:250px;z-index:1}
.hero-copy h1{font-size:24px;font-weight:800;color:var(--ink);line-height:1;white-space:nowrap}
.hero-copy .sub{font-size:8px;color:var(--green-dark);font-weight:700;margin:4px 0 8px;text-transform:uppercase}
.hero-copy ul{list-style:none;font-size:8.5px;color:#444}
.hero-copy li{padding-left:10px;position:relative;margin-bottom:2px}
.hero-copy li::before{content:"";position:absolute;left:0;top:4px;width:4px;height:4px;background:var(--green)}
.btn{display:inline-block;background:linear-gradient(var(--orange),var(--orange-dark));color:var(--white);font-weight:700;border-radius:3px}
.hero-copy .btn{margin-top:14px;font-size:11px;padding:6px 16px}
.hero-person{position:absolute;right:0;top:0;width:210px;height:190px;background:linear-gradient(135deg,#d7dde2,#a9b6bf)}
.hero-call{position:absolute;right:14px;bottom:8px;font-size:15px;font-weight:800;color:var(--green-dark);white-space:nowrap}
.hero-call span{color:var(--ink)}

/* tabs */
.plan-tabs{margin:8px 18px 0;display:flex;gap:4px;height:20px}
.plan-tabs a{font-size:10px;font-weight:800;line-height:20px;padding:0 14px;background:var(--orange);color:var(--white);border-radius:3px 3px 0 0}
.plan-tabs a.active{background:var(--white);color:var(--orange);border:1px solid var(--line);border-bottom:none}

/* cards */
.plans{margin:0 18px;height:150px;border:1px solid var(--line);background:var(--light);display:flex;padding:10px 14px;gap:14px}
.plan{flex:1;background:var(--white);border:1px solid var(--line);padding:8px 10px;position:relative}
.plan h3{font-size:11px;font-weight:700;text-align:center}
.plan-body{display:flex;gap:6px;margin-top:6px}
.plan-image{width:52px;height:60px;background:linear-gradient(#666,#222)}
.price{font-size:22px;font-weight:800;color:var(--ink);line-height:1}
.price small{font-size:7px;font-weight:600;display:block;color:var(--muted)}
.specs{font-size:6.5px;color:#666;margin-top:3px}
.plan-foot{position:absolute;left:10px;right:10px;bottom:8px;display:flex;justify-content:space-between;align-items:center;font-size:7px;color:#666}
.plan-foot .btn{font-size:8px;padding:3px 12px}

/* features */
.features{margin:8px 18px 0;height:88px;display:flex;align-items:center;gap:20px;padding-left:6px}
.feature-globe{width:70px;height:70px;border-radius:50%;background:radial-gradient(circle at 35% 35%,#9fd36a,#3f6a0c)}
.feature-list{list-style:none;display:grid;grid-template-columns:1fr 1fr;gap:7px 40px;font-size:8.5px;font-weight:600;color:#333}
.feature-list li{display:flex;align-items:center;gap:6px}
.feature-list svg{width:11px;height:11px}

/* quote */
.quote{margin:15px 18px 0;height:90px;position:relative;padding:4px 20px 0 56px;font-size:12.5px;font-weight:700;color:var(--green-dark);line-height:1.45;text-align:center}
.quote::before{content:"\201C";position:absolute;left:14px;top:-14px;font-size:64px;color:var(--green);font-weight:800}
.quote mark{background:var(--green);color:var(--white);padding:0 3px}

/* footer */
.site-footer{position:absolute;left:0;top:710px;width:691px;height:490px;background:var(--dark);color:#aaa}
.partners{height:38px;display:flex;justify-content:center;align-items:center;gap:14px;border-bottom:1px solid #333}
.partners span{width:52px;height:16px;background:#3a3a3a;border-radius:2px}
.footer-nav{height:18px;display:flex;justify-content:center;gap:14px;font-size:7px;line-height:18px;color:#bbb;background:var(--darker)}
.link-cols{display:flex;padding:6px 18px;gap:14px;height:64px}
.link-cols div{flex:1}
.link-cols h4{font-size:7px;color:var(--green);font-weight:700;text-transform:uppercase;margin-bottom:2px}
.link-cols p{font-size:6.5px;line-height:1.45}
.footer-lead{font-size:10px;font-weight:700;color:var(--white);padding:2px 18px}
.mini-grid{display:grid;grid-template-columns:repeat(3,1fr);gap:6px 14px;padding:5px 18px;height:62px}
.mini{display:flex;gap:6px;font-size:6.5px}
.mini i{flex:none;width:22px;height:22px;background:#444;border-radius:2px}
.info-cols{display:flex;gap:16px;padding:10px 18px 0;border-top:1px solid #333;height:156px}
.info-cols>div{flex:1}
.info-cols h4{font-size:10px;color:var(--white);font-weight:700;margin-bottom:4px}
.quick-links{list-style:none;font-size:7px;line-height:1.7}
.quick-links li::before{content:"» ";color:var(--green)}
.info-cols p{font-size:7px;line-height:1.55}
.footer-bottom{display:flex;justify-content:space-between;align-items:center;padding:0 18px;height:64px}
.footer-brand{display:flex;align-items:center;gap:6px}
.footer-brand i{width:18px;height:18px;background:var(--green)}
.footer-brand b{font-size:20px;font-weight:800;color:var(--white)}
.support{display:flex;align-items:center;gap:8px;background:#2d2d2d;padding:6px 12px;border-radius:4px}
.support svg{width:22px;height:22px}
.support b{display:block;font-size:10px;color:var(--white)}
.support span{font-size:11px;font-weight:800;color:var(--green)}
.copyright{height:40px;background:var(--darker);font-size:7px;line-height:40px;text-align:center;color:#777}
</style>
</head>
<body>
<header class="site-header">
  <div class="brand"><span class="brand-mark"></span><span class="brand-name">Zorpax</span></div>
  <div class="call-now">Call Now! <b>0.800.555.SRVR</b></div>
  <nav class="utility-links"><a href="#">Your Registration</a><a href="#">Customer Login</a><a href="#">Live Chat Online</a></nav>
</header>
<nav class="main-nav">
  <a class="active" href="#">Home</a><a href="#">Domains</a><a href="#">Web Hosting</a><a href="#">Latest News</a><a href="#">My Account</a><a href="#">Contact</a><a class="order" href="#">Order Now</a>
</nav>
<div class="announcement"><span class="pin"></span>Got an important announcement or a special offer? Tell our customers about it.<a href="#">Read More</a></div>

<section class="hero">
  <div class="hero-servers" role="img" aria-label="Rack of dedicated server hardware"></div>
  <div class="hero-badge">Get Free Setup</div>
  <div class="hero-person" role="img" aria-label="Photo of a smiling support agent with a headset"></div>
  <div class="hero-copy">
    <h1>Dedicated Servers</h1>
    <p class="sub">Powerful and reliable</p>
    <ul>
      <li>Pure Web Client for Terminal Server</li>
      <li>Pure Web Client for Terminal Server</li>
      <li>Pure Web Terminal Server</li>
      <li>Pure Web Client for Terminal Server</li>
      <li>Pure Web Client for Terminal Server</li>
    </ul>
    <a class="btn" href="#">Find Out More »</a>
  </div>
  <div class="hero-call">Call Sales Today <span>01234 567 890</span></div>
</section>

<nav class="plan-tabs"><a class="active" href="#">Dedicated Servers</a><a href="#">Web Hosting</a><a href="#">Virtual Private Servers</a></nav>
<section class="plans">
  <article class="plan">
    <h3>Corelite 2.4GHz</h3>
    <div class="plan-body"><div class="plan-image" role="img" aria-label="Server unit"></div><div><p class="price">$39.00<small>per month</small></p><p class="specs">512 MB RAM<br>80 GB HDD<br>1000 GB Traffic</p></div></div>
    <div class="plan-foot">All Dedicated Servers<a class="btn" href="#">Order</a></div>
  </article>
  <article class="plan">
    <h3>Corelite 2.4GHz</h3>
    <div class="plan-body"><div class="plan-image" role="img" aria-label="Server unit"></div><div><p class="price">$39.00<small>per month</small></p><p class="specs">512 MB RAM<br>80 GB HDD<br>1000 GB Traffic</p></div></div>
    <div class="plan-foot">All Dedicated Servers<a class="btn" href="#">Order</a></div>
  </article>
  <article class="plan">
    <h3>Corelite 2.4GHz</h3>
    <div class="plan-body"><div class="plan-image" role="img" aria-label="Server unit"></div><div><p class="price">$39.00<small>per month</small></p><p class="specs">512 MB RAM<br>80 GB HDD<br>1000 GB Traffic</p></div></div>
    <div class="plan-foot">All Dedicated Servers<a class="btn" href="#">Order</a></div>
  </article>
</section>

<section class="features">
  <div class="feature-globe" role="img" aria-label="Globe illustration"></div>
  <ul class="feature-list">
    <li><svg viewBox="0 0 12 12"><circle cx="6" cy="6" r="6" fill="#7cbd1e"/><path d="M3 6.2l2 2 4-4.4" stroke="#fff" stroke-width="1.6" fill="none"/></svg>100% Network Uptime SLA</li>
    <li><svg viewBox="0 0 12 12"><circle cx="6" cy="6" r="6" fill="#7cbd1e"/><path d="M3 6.2l2 2 4-4.4" stroke="#fff" stroke-width="1.6" fill="none"/></svg>3 SSAE-16 Certified Data Centers</li>
    <li><svg viewBox="0 0 12 12"><circle cx="6" cy="6" r="6" fill="#7cbd1e"/><path d="M3 6.2l2 2 4-4.4" stroke="#fff" stroke-width="1.6" fill="none"/></svg>ISO 9001:2008 Certified</li>
    <li><svg viewBox="0 0 12 12"><circle cx="6" cy="6" r="6" fill="#7cbd1e"/><path d="M3 6.2l2 2 4-4.4" stroke="#fff" stroke-width="1.6" fill="none"/></svg>Coast-to-Coast IP Backbone</li>
    <li><svg viewBox="0 0 12 12"><circle cx="6" cy="6" r="6" fill="#7cbd1e"/><path d="M3 6.2l2 2 4-4.4" stroke="#fff" stroke-width="1.6" fill="none"/></svg>24/7 TTL Technical Support</li>
    <li><svg viewBox="0 0 12 12"><circle cx="6" cy="6" r="6" fill="#7cbd1e"/><path d="M3 6.2l2 2 4-4.4" stroke="#fff" stroke-width="1.6" fill="none"/></svg>Award Winning Since 1998</li>
  </ul>
</section>

<blockquote class="quote"><mark>The standard chunk of Lorem Ipsum</mark> used since the 1500s is reproduced below for those interested. Sections 1.10.32 and 1.10.33 from "de Finibus Bonorum et Malorum" by Cicero are also chunk of Lorem Ipsum used since the 1500s is reproduced below in their exact original form</blockquote>

<footer class="site-footer">
  <div class="partners"><span></span><span></span><span></span><span></span><span></span><span></span><span></span><span></span><span></span></div>
  <nav class="footer-nav"><a href="#">Home</a><a href="#">Domains</a><a href="#">Web Hosting</a><a href="#">Latest News</a><a href="#">My Account</a><a href="#">Contact</a><a href="#">Order Now</a></nav>
  <div class="link-cols">
    <div><h4>Server Racks</h4><p>Rack cabinets and mounts<br>Power strips and cables<br>Cooling fan modules</p></div>
    <div><h4>Compliance</h4><p>Data center audits<br>Privacy and security<br>Uptime reporting</p></div>
    <div><h4>Client Tools</h4><p>Control panel access<br>Backup manager<br>Billing overview</p></div>
    <div><h4>Standard Links</h4><p>Plans and pricing<br>Network status<br>Knowledge base</p></div>
    <div><h4>Free Products</h4><p>Website builder trial<br>Email forwarding<br>Domain parking</p></div>
  </div>
  <p class="footer-lead">Lorem Ipsum has been the industry's standard dummy text ever since the 1500s</p>
  <div class="mini-grid">
    <div class="mini"><i></i><p>Lorem ipsum dolor sit amet, a galley of type was scrambled to make a type specimen book.</p></div>
    <div class="mini"><i></i><p>Lorem ipsum dolor sit amet, a galley of type was scrambled to make a type specimen book.</p></div>
    <div class="mini"><i></i><p>Lorem ipsum dolor sit amet, a galley of type was scrambled to make a type specimen book.</p></div>
    <div class="mini"><i></i><p>Lorem ipsum dolor sit amet, a galley of type was scrambled to make a type specimen book.</p></div>
    <div class="mini"><i></i><p>Lorem ipsum dolor sit amet, a galley of type was scrambled to make a type specimen book.</p></div>
    <div class="mini"><i></i><p>Lorem ipsum dolor sit amet, a galley of type was scrambled to make a type specimen book.</p></div>
  </div>
  <div class="info-cols">
    <div><h4>Quick Links</h4>
      <ul class="quick-links"><li>Effective evolving IT solutions</li><li>Effective evolving IT solutions</li><li>Effective evolving IT solutions</li><li>Effective evolving IT solutions</li><li>Effective evolving IT solutions</li><li>Effective evolving IT solutions</li><li>Effective evolving IT solutions</li></ul>
    </div>
    <div><h4>About Nimbus Services</h4>
      <p>Nimbus Services builds dependable hosting platforms for businesses of every size. Our engineers manage servers, networks and storage around the clock so our customers can focus on their websites and applications. We keep pricing simple and support personal.</p>
    </div>
    <div><h4>Information</h4>
      <p>The information on this page is general guidance only. Prices, features and availability may change without notice. Please contact our sales team before ordering.</p>
    </div>
  </div>
  <div class="footer-bottom">
    <div class="footer-brand"><i></i><b>Zorpax</b></div>
    <div class="support">
      <svg viewBox="0 0 24 24"><path d="M6 3l3 0 1.5 5-2 1.5a11 11 0 0 0 6 6l1.5-2 5 1.5 0 3a2 2 0 0 1-2 2A17 17 0 0 1 4 5a2 2 0 0 1 2-2z" fill="#7cbd1e"/></svg>
      <div><b>Need Support?</b><span>+44 1234 000 111</span></div>
    </div>
  </div>
  <div class="copyright">Copyright © Zorpax.com. All rights reserved.</div>
</footer>
</body>
</html>
```